Brightwall painting and decorating *

Need a flyer design to advertise my services
So the information I need included is the services we offer at brightwall painting and decorating which include
Interior painting
Exterior painting
Wallpaper hanging
Paint and cellulose spraying
Dust free sanding
Pressure washing
Stone cleaning
Also would need to have my company contact details in
Www.brightwallpaintingdecorating.co.uk
Email is info@brightwallpaintingdecorating.com
Brightwall Painting & Decorating Services has a proven track record of innovative designs, effective problem solving and attention to detail and our goal is to meet and exceed the expectations of every customer. We take on all types of jobs from small domestic work to larger commercial projects, all carried out to the highest standards, and at very competitive prices.
Colors
Designer to choose colors to be used in the design.
Look and feel

```html
<!DOCTYPE html>
<html lang="en">
<head>
<meta charset="utf-8">
<title>Brightwall Painting and Decorating – Flyer</title>
<link rel="stylesheet" href="https://fonts.googleapis.com/css2?family=Open+Sans:wght@400;600;700&display=swap">
<style>
  :root{
    --page-bg:#d9dde1;
    --paper:#f1f2f4;
    --navy:#1d4f7c;
    --brand-blue:#1f5f99;
    --sky:#2a90b8;
    --list-blue:#2a5d9e;
    --body-text:#3f5f80;
    --band-light:#8fd0ec;
    --band-mid:#2f97c4;
    --band-deep:#2a5fb0;
    --contact:#1b73a6;
    --footer:#3b3b3b;
    --white:#ffffff;
  }
  *{box-sizing:border-box;margin:0;padding:0}
  html,body{width:1040px;height:1200px;overflow:hidden}
  body{background:var(--page-bg);font-family:"Open Sans",Arial,sans-serif;position:relative}
  .flyer{position:absolute;left:70px;top:19px;width:900px;height:1163px;background:linear-gradient(#ffffff,var(--paper) 60%);overflow:hidden;box-shadow:0 6px 24px rgba(0,0,0,.18)}
  .flyer svg{position:absolute;left:0;top:0;width:900px;height:1163px}
  .brand{position:absolute;left:86px;top:44px;color:var(--brand-blue);font-weight:700;line-height:1}
  .brand__name{display:block;font-size:37px;letter-spacing:.5px}
  .brand__tagline{display:block;font-size:11px;margin-top:6px;letter-spacing:.2px}
  .headline{position:absolute;left:0;width:900px;top:462px;text-align:center;line-height:1;font-weight:400}
  .headline__main{display:block;font-size:47px;font-weight:400;color:var(--navy);letter-spacing:1.5px}
  .headline__outline{color:var(--white);-webkit-text-stroke:1.6px var(--navy)}
  .headline__sub{display:block;font-size:37px;font-weight:400;color:var(--sky);margin-top:8px;padding-left:8px;letter-spacing:1px}
  .gallery__item{position:absolute;top:552px;width:228px;height:228px;border-radius:50%;border:3px solid var(--sky);padding:6px;background:var(--white)}
  .gallery__photo{width:100%;height:100%;border-radius:50%}
  .gallery__item--office{left:68px}
  .gallery__item--office .gallery__photo{background:linear-gradient(#dfe6ea,#9aa0a3 55%,#6c6e70)}
  .gallery__item--lounge{left:344px}
  .gallery__item--lounge .gallery__photo{background:linear-gradient(#f5c654,#f0b63b 60%,#c89a60 85%,#b07a45)}
  .gallery__item--living{left:621px}
  .gallery__item--living .gallery__photo{background:linear-gradient(#e6d8bf,#b9a58c 50%,#d9d3cc 80%,#8a8580)}
  .services__title{position:absolute;left:0;width:862px;top:784px;text-align:center;font-size:28px;font-weight:400;color:var(--sky);letter-spacing:1px;line-height:1.2}
  .services__list{position:absolute;top:830px;list-style:none}
  .services__list--left{left:73px}
  .services__list--right{left:445px}
  .services__list li{position:relative;padding-left:30px;height:25px;line-height:21px;font-size:17px;font-weight:600;color:var(--list-blue);letter-spacing:3.2px}
  .services__list li::before{content:"";position:absolute;left:0;top:9px;width:9px;height:9px;border-radius:50%;background:var(--list-blue)}
  .about{position:absolute;left:73px;top:936px;width:754px;font-size:12.5px;line-height:16px;color:var(--body-text);text-align:center}
  .contact{position:absolute;left:0;top:1013px;width:900px;height:106px;background:var(--contact) repeating-linear-gradient(-60deg,rgba(255,255,255,0) 0 14px,rgba(255,255,255,.1) 14px 17px);text-align:center;color:var(--white)}
  .contact__phone{display:block;font-size:44px;font-weight:700;margin-top:14px;line-height:1}
  .contact__email{display:block;font-size:21px;margin-top:8px}
  .footer{position:absolute;left:0;top:1119px;width:900px;height:44px;background:var(--footer);color:var(--white);text-align:center;line-height:44px;font-size:18px;letter-spacing:4px}
</style>
</head>
<body>
<main class="flyer">
  <svg class="hero-photo" viewBox="0 0 966 1248" preserveAspectRatio="none" role="img" aria-label="Photo of a bright modern office with glass partitions, a sculpted white feature wall and a yellow lounge chair">
    <defs>
      <linearGradient id="heroTone" x1="0" y1="0" x2="1" y2="1">
        <stop offset="0" stop-color="#e9f1f5"/>
        <stop offset=".45" stop-color="#c6d9e2"/>
        <stop offset="1" stop-color="#7f9eae"/>
      </linearGradient>
    </defs>
    <path d="M0,410 C200,360 400,390 560,450 C720,510 860,480 966,320 V0 H0 Z" fill="url(#heroTone)"/>
  </svg>
  <svg class="wave-bands" viewBox="0 0 966 1248" preserveAspectRatio="none" aria-hidden="true">
    <path d="M0,420 C200,365 410,385 565,445 C725,505 870,480 966,330 L966,380 C880,520 720,530 560,490 C400,450 200,405 0,455 Z" fill="var(--band-light)"/>
    <path d="M0,445 C200,395 400,425 560,480 C720,530 880,520 966,375 L966,440 C890,560 720,575 560,540 C400,500 200,430 0,490 Z" fill="var(--band-mid)"/>
    <path d="M0,472 C200,415 400,440 560,500 C720,555 890,545 966,430 L966,470 C900,575 740,590 580,560 C400,520 200,440 0,500 Z" fill="var(--band-deep)"/>
  </svg>

  <div class="brand">
    <span class="brand__name">BRIGHTWALL</span>
    <span class="brand__tagline">PAINTING AND DECORATING SERVICES</span>
  </div>

  <h1 class="headline">
    <span class="headline__main">ESTABLISHED <span class="headline__outline">DECORATORS</span></span>
    <span class="headline__sub">IN SOUTH LONDON</span>
  </h1>

  <div class="gallery">
    <div class="gallery__item gallery__item--office"><div class="gallery__photo" role="img" aria-label="Photo of a freshly decorated office lounge with grey sofas"></div></div>
    <div class="gallery__item gallery__item--lounge"><div class="gallery__photo" role="img" aria-label="Photo of a yellow painted wall with a sofa and plant"></div></div>
    <div class="gallery__item gallery__item--living"><div class="gallery__photo" role="img" aria-label="Photo of a living room with papered feature wall and cream sofas"></div></div>
  </div>

  <h2 class="services__title">OUR RANGE OF SERVICES INCLUDE:</h2>
  <ul class="services__list services__list--left">
    <li>INTERIOR PAINTING</li>
    <li>EXTERIOR PAINTING</li>
    <li>WALLPAPER HANGING</li>
    <li>DUST FREE SANDING</li>
  </ul>
  <ul class="services__list services__list--right">
    <li>PAINT AND CELLULOSE SPRAYING</li>
    <li>PRESSURE WASHING</li>
    <li>STONE CLEANING</li>
  </ul>

  <p class="about">Brightwall Painting &amp; Decorating Services has a proven track record of innovative designs, effective problem solving and attention to detail and our goal is to meet and exceed the expectations of every customer. We take on all types of jobs from small domestic work to larger commercial projects, all carried out to the highest standards, and at very competitive prices.</p>

  <div class="contact">
    <span class="contact__phone">07700 900 482</span>
    <span class="contact__email">EMAIL INFO@BRIGHTWALLPAINTINGDECORATING.COM</span>
  </div>
  <div class="footer">WWW.BRIGHTWALLPAINTINGDECORATING.CO.UK</div>
</main>
</body>
</html>
```